Business Card Design

We need a business card that reflects a company that has been established for over 20 years, a card that displays confidence.
Although we are established we are forward thinking and always pushing forward.
Our company buys, processes and exports scrap metal all over the world.
We buy metal from all around Australia, although we sell it all across the globe.
The card should look modern, bold, but not over complicated.
Incorporate the Logo and the company colors.
Would like to see in raised lettering.
Updates

Thank you to all designers, same amazing designs in such a short time.

At this stage designer Porvil is the front runner.
The design is crisp, clean and modern, not to busy.
I would like to see what you all come up with in the next 24 hours.
Thank you

Industry/Entity Type

Business

Contact Information for Business Card

Dunmore Metal Recyclers
Greg Pavlenko
Director
3-7 Wandle Road
Burton, South Australia 5110
Phone +61-8-8357-4120
Fax +61-8-8357 1934
Mobile 0429 513 806
email: greg@dunmoremr.example
web: www.dunmoremr.example

```html
<!DOCTYPE html>
<html lang="en">
<head>
<meta charset="utf-8">
<title>Dunmore Metal Recyclers – Business Card</title>
<link rel="stylesheet" href="https://fonts.googleapis.com/css2?family=Arimo:wght@400;700&display=swap">
<style>
  :root {
    --page-bg: #e6e6e3;
    --card-black: #0b0b0b;
    --green: #3d8b35;
    --green-light: #6fa868;
    --text-white: #f4f4f4;
    --rule: #9a9a9a;
  }
  * { box-sizing: border-box; margin: 0; padding: 0; }
  html, body {
    width: 1200px; height: 822px; overflow: hidden;
    background: var(--page-bg);
    font-family: "Arimo", Arial, sans-serif;
  }
  .card {
    position: absolute; left: 100px; top: 126px;
    width: 1000px; height: 570px;
    background: var(--card-black);
    border-radius: 4px; overflow: hidden;
    box-shadow: 0 10px 30px rgba(0,0,0,.25);
    color: var(--text-white);
  }
  .card__swooshes { position: absolute; inset: 0; }
  .contact { position: absolute; left: 80px; top: 60px; width: 380px; }
  .contact__name { font-size: 38px; font-weight: 700; letter-spacing: .3px; }
  .contact__title { font-size: 22px; text-align: right; margin-top: 4px; padding-right: 30px; }
  .contact__rule { border-top: 2px dashed var(--rule); margin: 22px 0 20px; }
  .contact__row { display: flex; align-items: center; gap: 16px; font-size: 24px; line-height: 36px; }
  .contact__row svg { width: 20px; height: 20px; flex: none; fill: var(--text-white); }
  .contact__row--indent { padding-left: 36px; }
  .brand {
    position: absolute; left: 560px; top: 170px; width: 380px;
    display: flex; flex-direction: column; align-items: center; gap: 26px;
  }
  .brand__mark { width: 130px; height: 130px; border-radius: 50%; background: var(--green); }
  .brand__name { font-size: 34px; font-weight: 700; text-align: center; line-height: 1.2; color: var(--text-white); }
</style>
</head>
<body>
<main class="card">
  <svg class="card__swooshes" viewBox="0 0 1000 570" aria-hidden="true">
    <path d="M470 0 Q760 95 1000 38 L1000 0 Z" fill="var(--green)"/>
    <path d="M0 390 C20 545 250 545 430 495 C330 565 200 570 0 570 Z" fill="var(--green)"/>
  </svg>

  <section class="contact">
    <h1 class="contact__name">Greg Pavlenko</h1>
    <p class="contact__title">Director</p>
    <div class="contact__rule"></div>

    <p class="contact__row">
      <svg viewBox="0 0 20 20"><path d="M10 1a6 6 0 0 0-6 6c0 4.5 6 12 6 12s6-7.5 6-12a6 6 0 0 0-6-6zm0 8.5A2.5 2.5 0 1 1 10 4.5a2.5 2.5 0 0 1 0 5z"/></svg>
      3-7 Wandle Road Burton,
    </p>
    <p class="contact__row contact__row--indent">South Australia 5110</p>
    <div class="contact__rule"></div>

    <p class="contact__row">
      <svg viewBox="0 0 20 20"><path d="M4 2l3 0 2 5-2 1.5c1 2 2.5 3.5 4.5 4.5L13 11l5 2v3c0 1-1 2-2 2C8.5 18 2 11.5 2 4c0-1 1-2 2-2z"/></svg>
      +61-8-8357-4120
    </p>
    <p class="contact__row">
      <svg viewBox="0 0 20 20"><path d="M5 2h10v5H5zM2 8h16v7h-3v3H5v-3H2zm5 5v3h6v-3z"/></svg>
      +61-8-8357 1934
    </p>
    <p class="contact__row">
      <svg viewBox="0 0 20 20"><path d="M6 1h8a1 1 0 0 1 1 1v16a1 1 0 0 1-1 1H6a1 1 0 0 1-1-1V2a1 1 0 0 1 1-1zm1 2v12h6V3zm3 13.2a.9.9 0 1 0 0 1.8.9.9 0 0 0 0-1.8z"/></svg>
      0429 513 806
    </p>
    <div class="contact__rule"></div>

    <p class="contact__row">
      <svg viewBox="0 0 20 20"><path d="M2 4h16v12H2zm1.5 1.5v.4L10 11l6.5-5.1v-.4zm0 2.3v6.7h13V7.8L10 13z"/></svg>
      greg@dunmoremr.example
    </p>
    <p class="contact__row">
      <svg viewBox="0 0 20 20"><path d="M10 1a9 9 0 1 0 0 18 9 9 0 0 0 0-18zm0 1.6c.9 0 2.2 1.9 2.6 5.4H7.4C7.8 4.5 9.1 2.6 10 2.6zM7.3 9.5h5.4c0 .4 0 .7 0 1s0 .6 0 1H7.3c0-.4 0-.7 0-1s0-.6 0-1zM2.7 9.5h3.1v2H2.7a7.4 7.4 0 0 1 0-2zm11.5 0h3.1a7.4 7.4 0 0 1 0 2h-3.1zM7.4 13h5.2c-.4 3.5-1.7 5.4-2.6 5.4S7.8 16.5 7.4 13z"/></svg>
      www.dunmoremr.example
    </p>
  </section>

  <section class="brand">
    <div class="brand__mark"></div>
    <p class="brand__name">Dunmore Metal Recyclers</p>
  </section>
</main>
</body>
</html>
```